Business card - Kite Harbor - size 85 mm * 55 mm

We need new business cards. Design must fit with our vision of the firm. You find in the attached file our logo and a short description of our firm (mission, vision, value, business and so on).

Target Market(s)

Consulting firm in performance improvement

Industry/Entity Type

Management Consulting

Contact Information for Business Card

SIZE
85 mm * 55 mm
INFORMATIONS
name surname
role position
telephone number
email address

Requirements
Must have
• the brand must APPEAR for the rest Would we like to have something sleek, inspired to a "just right" approach
Should not have
• Please avoid the black color as background

```html
<!DOCTYPE html>
<html lang="en">
<head>
<meta charset="utf-8">
<title>Kite Harbor – Business Cards</title>
<link rel="stylesheet" href="https://fonts.googleapis.com/css2?family=Questrial&display=swap">
<style>
  :root {
    --stage: #3b3b3d;
    --card-dark: #3f3f41;
    --card-light: #ffffff;
    --brand-green: #8cc63f;
    --text-light: #f2f2f2;
    --shadow: rgba(0, 0, 0, 0.35);
  }
  * { box-sizing: border-box; margin: 0; padding: 0; }
  html, body {
    width: 1200px;
    height: 810px;
    overflow: hidden;
    background: var(--stage);
    font-family: "Questrial", Arial, sans-serif;
  }
  .stage {
    position: relative;
    width: 1200px;
    height: 810px;
    display: flex;
    align-items: center;
    justify-content: center;
    gap: 60px;
  }
  .card {
    position: relative;
    width: 520px;
    height: 336px;
    border-radius: 22px;
    overflow: hidden;
    box-shadow: 0 10px 28px var(--shadow);
  }
  .card--front { background: var(--card-dark); }
  .card--back { background: var(--card-dark); }

  .brand {
    position: absolute;
    display: flex;
    flex-direction: column;
    align-items: center;
    gap: 22px;
  }
  .brand__dot {
    width: 62px;
    height: 62px;
    border-radius: 50%;
    border: 4px solid var(--brand-green);
  }
  .brand__name {
    color: var(--brand-green);
    font-size: 30px;
    letter-spacing: 0.55em;
    margin-right: -0.55em;
    white-space: nowrap;
    text-transform: uppercase;
  }
  .card--front .brand {
    left: 0; right: 0; top: 92px;
  }

  .back__art {
    position: absolute;
    inset: 0;
  }
  .card--back .brand {
    left: 20px;
    width: 250px;
    top: 110px;
    gap: 18px;
  }
  .card--back .brand__dot { width: 46px; height: 46px; border-width: 3px; }
  .card--back .brand__name { font-size: 19px; letter-spacing: 0.45em; margin-right: -0.45em; }

  .contact {
    position: absolute;
    left: 346px;
    top: 96px;
    color: var(--text-light);
  }
  .contact__name {
    color: var(--brand-green);
    font-size: 21px;
    line-height: 1.1;
  }
  .contact__role {
    font-size: 13px;
    margin-top: 4px;
  }
  .contact__list {
    list-style: none;
    margin-top: 18px;
    font-size: 12.5px;
    line-height: 1.7;
  }
  .contact__item {
    display: flex;
    align-items: center;
    gap: 7px;
  }
  .contact__icon {
    width: 12px;
    height: 12px;
    fill: var(--brand-green);
    flex: none;
  }
</style>
</head>
<body>
<main class="stage">
  <section class="card card--front" aria-label="Card front">
    <div class="brand">
      <span class="brand__dot"></span>
      <span class="brand__name">Kite Harbor</span>
    </div>
  </section>

  <section class="card card--back" aria-label="Card back">
    <svg class="back__art" viewBox="0 0 520 336" aria-hidden="true">
      <path d="M0 0 H215 C 290 40 322 170 322 336 H0 Z" fill="var(--card-light)"/>
      <path d="M215 0 C 290 40 322 170 322 336" fill="none" stroke="var(--brand-green)" stroke-width="4"/>
      <path d="M0 0 H212 C 285 40 316 170 316 336 H0 Z" fill="var(--card-light)"/>
    </svg>
    <div class="brand">
      <span class="brand__dot"></span>
      <span class="brand__name">Kite Harbor</span>
    </div>
    <div class="contact">
      <p class="contact__name">Adrian Moreau</p>
      <p class="contact__role">President</p>
      <ul class="contact__list">
        <li class="contact__item">
          <svg class="contact__icon" viewBox="0 0 24 24" aria-hidden="true"><path d="M6.6 10.8a15.1 15.1 0 0 0 6.6 6.6l2.2-2.2a1 1 0 0 1 1-.25 11.4 11.4 0 0 0 3.6.57 1 1 0 0 1 1 1V20a1 1 0 0 1-1 1A17 17 0 0 1 3 4a1 1 0 0 1 1-1h3.5a1 1 0 0 1 1 1c0 1.25.2 2.45.57 3.57a1 1 0 0 1-.25 1z"/></svg>
          <span>0412555819</span>
        </li>
        <li class="contact__item">
          <svg class="contact__icon" viewBox="0 0 24 24" aria-hidden="true"><path d="M2 5h20v14H2z M3.5 6.5 12 13l8.5-6.5" fill="var(--brand-green)" stroke="var(--card-dark)" stroke-width="1.5"/></svg>
          <span>Contact@kiteharbor.com</span>
        </li>
      </ul>
    </div>
  </section>
</main>
</body>
</html>
```